Contest - label design for a health related product with 4 color variations

Nuvera-Store (http://www.nuvera-store.example) is an online shop selling health related products and nutritional supplements, such as algae products, wheat grass and barley grass powder. These products have a positive impact on a person's health. Through Craft Huddle, we have designed already a logo for the shop and now we need to create labels that will be placed on a brown glass bottle (see attachment). The logo shall be used without the slogan 'One life. Live it healthy.' when creating the label.

Your job is to design a label with 4 color variations, blue, green, red and yellow. The measurements of the label is 80 mm x 173 mm, but please add 3 mm bleed to each side.

The information that has to go on the label can be taken from the attachment 'label information.pdf'. For the sake of communication, we will divide the label into 3 parts

- left
- middle
- right

The left part and the right part are fixed as this contains legal information. Please use easy to read fonts, non-serifed fonts, such as Arial, Verdana, Calibri. The left part contains a table and if Illustrator provides the possibility for tables, please use it as we need to be able to easily add and remove rows of the table.

The middle part contains the product description, the product quantity (i.e. 100 g), our logo without the slogan 'One live. Live it healthy.' and logos indicating the organic quality of the product (please see attachments). For the product name (i.e. QUB-Tangen) and the quantity (i.e. 100 Tabletten, 200 g) use the attached Lato font. Please note that the vertical position of our logo, the product name and the organic logos has NOT been set yet. You are free to position them where ever you feel in the middle part of the label.

Target Market(s)

Health concious people between 25 and 70

Industry/Entity Type

Health

Requirements
Must have
• - the attached logo without the slogan "One life...."
- the following attributes: healthy, joyful, vivid, lively, abstract, minimalistic
- colors that go along with our logo and the website www.nuvera-store.example
- all fonts need to be editable and not rendered
- the left part should have an editable table where we can add rows if necessary
- the attached font for product name and quantity
- 3 mm bleed on each side, so the final design is 6 mm wider and higher
- the final design will be in editable Illustrator files of a recent version.
Should not have
• - many overlaying, confusing lines or layers
- dark colors
- heavy appearance

```html
<!DOCTYPE html>
<html lang="de">
<head>
<meta charset="utf-8">
<title>QUB-Tangen – Etiketten in vier Farben</title>
<link rel="stylesheet" href="https://fonts.googleapis.com/css2?family=Lato:wght@700;900&family=Open+Sans:wght@400;700&display=swap">
<style>
  :root {
    --green: #0b9a55;
    --red: #c1141f;
    --yellow: #f7ab2f;
    --blue: #1b73ba;
    --orange: #f8b133;
    --paper: #ffffff;
    --ink-dark: #2b2b2b;
    --backdrop-light: #fbfbfb;
    --backdrop-dark: #dcdde0;
  }
  * { box-sizing: border-box; margin: 0; padding: 0; }
  html, body { width: 1200px; height: 900px; overflow: hidden; }
  body {
    background: radial-gradient(ellipse at center, var(--backdrop-light) 0%, #eeeff1 55%, var(--backdrop-dark) 100%);
    font-family: "Open Sans", Arial, sans-serif;
    position: relative;
  }

  .label {
    position: absolute;
    width: 491px;
    height: 228px;
    box-shadow: 2px 3px 5px rgba(0,0,0,.35);
    overflow: hidden;
    color: var(--ink-dark);
  }
  .label--green  { --main: var(--green);  --accent: var(--orange); --swirl-a: #f7a52c; --swirl-b: #fde3b5; --side-ink: #fff; }
  .label--red    { --main: var(--red);    --accent: var(--orange); --swirl-a: #f7a52c; --swirl-b: #fde3b5; --side-ink: #fff; }
  .label--yellow { --main: var(--yellow); --accent: var(--green);  --swirl-a: #1f9b62; --swirl-b: #cfe9dc; --side-ink: #3a2a10; }
  .label--blue   { --main: var(--blue);   --accent: var(--green);  --swirl-a: #1f9b62; --swirl-b: #cfe9dc; --side-ink: #fff; }

  .pos-tl { left: 62px;  top: 28px; }
  .pos-tr { left: 655px; top: 28px; }
  .pos-bl { left: 62px;  top: 636px; }
  .pos-br { left: 655px; top: 636px; }

  .label__shape { position: absolute; inset: 0; }
  .shape-main   { fill: var(--main); }
  .shape-accent { fill: var(--accent); }
  .shape-paper  { fill: var(--paper); }

  .swirl {
    position: absolute;
    left: 180px; top: 42px;
    width: 150px; height: 150px;
    border-radius: 50%;
    background: radial-gradient(circle at 50% 50%, var(--paper) 0%, var(--swirl-b) 35%, var(--swirl-a) 100%);
    opacity: .55;
  }

  /* left: legal table */
  .facts {
    position: absolute;
    left: 4px; top: 18px;
    width: 156px;
    border: 1px solid var(--main);
    background: var(--paper);
    font-size: 4.8px;
    line-height: 1.3;
  }
  .facts table { width: 100%; border-collapse: collapse; }
  .facts th {
    background: var(--main);
    color: #fff;
    font-weight: 700;
    font-size: 5px;
    padding: 1.5px 3px;
    text-align: left;
  }
  .facts th.center, .facts td.center { text-align: center; }
  .facts th.right,  .facts td.right  { text-align: right; }
  .facts td { padding: 3px 3px; vertical-align: top; }
  .facts .gap td { height: 40px; padding-top: 6px; }
  .facts .nutri td { height: 46px; padding-top: 6px; }
  .facts .vitamin td { height: 18px; vertical-align: middle; }

  .distributor {
    position: absolute;
    left: 4px; top: 158px;
    width: 156px;
    text-align: center;
    font-style: normal;
    font-size: 4.8px;
    line-height: 1.3;
  }
  .distributor strong { display: block; font-size: 5px; }

  .web {
    position: absolute;
    left: 12px; top: 207px;
    font-weight: 700;
    font-size: 11px;
    color: #fff;
  }

  /* middle */
  .brand {
    position: absolute;
    left: 196px; top: 4px;
    width: 116px; height: 28px;
    display: flex; align-items: center; justify-content: center; gap: 4px;
    background: var(--paper);
    border-radius: 0 0 14px 14px;
    font-weight: 700;
    font-size: 9.5px;
    color: var(--green);
  }
  .brand__dot { width: 7px; height: 7px; border-radius: 50%; background: var(--orange); }
  .product {
    position: absolute;
    left: 180px; top: 74px;
    width: 150px;
    text-align: center;
    font-family: "Lato", Arial, sans-serif;
    font-weight: 900;
    font-size: 18px;
    line-height: 1.2;
    color: var(--main);
  }
  .quantity {
    position: absolute;
    left: 180px; top: 98px;
    width: 150px;
    text-align: center;
    font-family: "Lato", Arial, sans-serif;
    font-weight: 700;
    font-size: 8px;
    color: var(--main);
  }
  .badges { position: absolute; left: 211px; top: 166px; display: flex; gap: 6px; }
  .badge-eu  { width: 22px; height: 17px; background: #8cc63e; }
  .badge-bio { width: 19px; height: 19px; border-radius: 50%; border: 1.5px solid #444; background: var(--paper); }

  /* right: usage and notes */
  .notes {
    position: absolute;
    left: 336px;
    width: 148px;
    color: var(--side-ink);
    font-size: 4.8px;
    line-height: 1.35;
  }
  .notes--usage  { top: 28px; }
  .notes--hints  { top: 70px; }
  .notes--expiry { top: 190px; }
  .notes h3 {
    color: #fff;
    text-align: center;
    font-size: 6.6px;
    font-weight: 700;
    margin-bottom: 6px;
  }
  .notes ul { list-style: none; }
  .notes li { padding-left: 5px; text-indent: -4px; }
  .notes li::before { content: "• "; }
  .notes .center { text-align: center; }
</style>
</head>
<body>

<!-- green -->
<article class="label label--green pos-tl">
  <svg class="label__shape" viewBox="0 0 491 228" width="491" height="228" aria-hidden="true">
    <rect class="shape-main" width="491" height="228"/>
    <rect class="shape-accent" width="491" height="14"/>
    <path class="shape-accent" d="M120,206 C250,206 330,180 335,110 C345,185 290,212 210,212 L120,212 Z"/>
    <path class="shape-paper" d="M0,14 H250 C305,18 334,70 330,118 C326,170 285,200 210,204 H0 Z"/>
  </svg>
  <div class="swirl" role="img" aria-label="Abstrakte Spirale in Orangetönen"></div>
  <section class="facts">
    <table>
      <tr><th colspan="3" class="center">Zutaten</th></tr>
      <tr class="gap"><td colspan="3">QUB-Tangen (QUB - Aphanizomenon Flos Aqua) aus dem Klamath Lake, bei 37° Celsius getrocknet.</td></tr>
      <tr><th>Nährwertangaben</th><th class="center">in 100g</th><th class="right">pro Kapsel</th></tr>
      <tr class="nutri"><td colspan="3">Kohlenhydrate<br>Fett<br>Eiweiß<br>Brennwert (kJ / kcal)</td></tr>
      <tr><th>Inhaltsstoffe</th><th class="center">pro Kapsel</th><th class="right">% RDA</th></tr>
      <tr class="vitamin"><td>Vitamin C</td><td class="center">50,2 mg</td><td class="right">50%</td></tr>
    </table>
  </section>
  <address class="distributor"><strong>Vertrieb</strong>Lindor Marsh Trading<br>Weidenhof-Gasse 12<br>1230 Wien<br>Österreich</address>
  <div class="web">www.nuvera-store.example</div>
  <div class="brand"><span class="brand__dot"></span>Nuvera-Store</div>
  <h2 class="product">QUB-Tangen</h2>
  <div class="quantity">100 Tabletten</div>
  <div class="badges"><span class="badge-eu"></span><span class="badge-bio"></span></div>
  <section class="notes notes--usage">
    <h3>Verzehrempfehlung</h3>
    <p class="center">3 x täglich 3 - 5 Tabletten unzerkaut mit Wasser zu den Mahlzeiten einnehmen.</p>
  </section>
  <section class="notes notes--hints">
    <h3>Hinweise</h3>
    <ul>
      <li>Die angegebene tägliche Verzehrmenge sollte nicht überschritten werden.</li>
      <li>Nahrungsergänzungsmittel sind kein Ersatz für eine ausgewogene und abwechslungsreiche Ernährung.</li>
      <li>Das Produkt lichtgeschützt, verschlossen und außerhalb der Reichweite von kleinen Kindern aufbewahren.</li>
      <li>Während der Schwangerschaft und Stillzeiten sollte vor dem Verzehr von Nahrungsergän­zungsmitteln ein Arzt konsultiert werden.</li>
    </ul>
  </section>
  <section class="notes notes--expiry">
    <h3>Mindesthaltbarkeitsdatum</h3>
    <p>Siehe Boden.</p>
  </section>
</article>

<!-- red -->
<article class="label label--red pos-tr">
  <svg class="label__shape" viewBox="0 0 491 228" width="491" height="228" aria-hidden="true">
    <rect class="shape-main" width="491" height="228"/>
    <rect class="shape-accent" width="491" height="14"/>
    <path class="shape-accent" d="M120,206 C250,206 330,180 335,110 C345,185 290,212 210,212 L120,212 Z"/>
    <path class="shape-paper" d="M0,14 H250 C305,18 334,70 330,118 C326,170 285,200 210,204 H0 Z"/>
  </svg>
  <div class="swirl" role="img" aria-label="Abstrakte Spirale in Orangetönen"></div>
  <section class="facts">
    <table>
      <tr><th colspan="3" class="center">Zutaten</th></tr>
      <tr class="gap"><td colspan="3">QUB-Tangen (QUB - Aphanizomenon Flos Aqua) aus dem Klamath Lake, bei 37° Celsius getrocknet.</td></tr>
      <tr><th>Nährwertangaben</th><th class="center">in 100g</th><th class="right">pro Kapsel</th></tr>
      <tr class="nutri"><td colspan="3">Kohlenhydrate<br>Fett<br>Eiweiß<br>Brennwert (kJ / kcal)</td></tr>
      <tr><th>Inhaltsstoffe</th><th class="center">pro Kapsel</th><th class="right">% RDA</th></tr>
      <tr class="vitamin"><td>Vitamin C</td><td class="center">50,2 mg</td><td class="right">50%</td></tr>
    </table>
  </section>
  <address class="distributor"><strong>Vertrieb</strong>Lindor Marsh Trading<br>Weidenhof-Gasse 12<br>1230 Wien<br>Österreich</address>
  <div class="web">www.nuvera-store.example</div>
  <div class="brand"><span class="brand__dot"></span>Nuvera-Store</div>
  <h2 class="product">QUB-Tangen</h2>
  <div class="quantity">100 Tabletten</div>
  <div class="badges"><span class="badge-eu"></span><span class="badge-bio"></span></div>
  <section class="notes notes--usage">
    <h3>Verzehrempfehlung</h3>
    <p class="center">3 x täglich 3 - 5 Tabletten unzerkaut mit Wasser zu den Mahlzeiten einnehmen.</p>
  </section>
  <section class="notes notes--hints">
    <h3>Hinweise</h3>
    <ul>
      <li>Die angegebene tägliche Verzehrmenge sollte nicht überschritten werden.</li>
      <li>Nahrungsergänzungsmittel sind kein Ersatz für eine ausgewogene und abwechslungsreiche Ernährung.</li>
      <li>Das Produkt lichtgeschützt, verschlossen und außerhalb der Reichweite von kleinen Kindern aufbewahren.</li>
      <li>Während der Schwangerschaft und Stillzeiten sollte vor dem Verzehr von Nahrungsergän­zungsmitteln ein Arzt konsultiert werden.</li>
    </ul>
  </section>
  <section class="notes notes--expiry">
    <h3>Mindesthaltbarkeitsdatum</h3>
    <p>Siehe Boden.</p>
  </section>
</article>

<!-- yellow -->
<article class="label label--yellow pos-bl">
  <svg class="label__shape" viewBox="0 0 491 228" width="491" height="228" aria-hidden="true">
    <rect class="shape-main" width="491" height="228"/>
    <rect class="shape-accent" width="491" height="14"/>
    <path class="shape-accent" d="M120,206 C250,206 330,180 335,110 C345,185 290,212 210,212 L120,212 Z"/>
    <path class="shape-paper" d="M0,14 H250 C305,18 334,70 330,118 C326,170 285,200 210,204 H0 Z"/>
  </svg>
  <div class="swirl" role="img" aria-label="Abstrakte Spirale in Grüntönen"></div>
  <section class="facts">
    <table>
      <tr><th colspan="3" class="center">Zutaten</th></tr>
      <tr class="gap"><td colspan="3">QUB-Tangen (QUB - Aphanizomenon Flos Aqua) aus dem Klamath Lake, bei 37° Celsius getrocknet.</td></tr>
      <tr><th>Nährwertangaben</th><th class="center">in 100g</th><th class="right">pro Kapsel</th></tr>
      <tr class="nutri"><td colspan="3">Kohlenhydrate<br>Fett<br>Eiweiß<br>Brennwert (kJ / kcal)</td></tr>
      <tr><th>Inhaltsstoffe</th><th class="center">pro Kapsel</th><th class="right">% RDA</th></tr>
      <tr class="vitamin"><td>Vitamin C</td><td class="center">50,2 mg</td><td class="right">50%</td></tr>
    </table>
  </section>
  <address class="distributor"><strong>Vertrieb</strong>Lindor Marsh Trading<br>Weidenhof-Gasse 12<br>1230 Wien<br>Österreich</address>
  <div class="web">www.nuvera-store.example</div>
  <div class="brand"><span class="brand__dot"></span>Nuvera-Store</div>
  <h2 class="product">QUB-Tangen</h2>
  <div class="quantity">100 Tabletten</div>
  <div class="badges"><span class="badge-eu"></span><span class="badge-bio"></span></div>
  <section class="notes notes--usage">
    <h3>Verzehrempfehlung</h3>
    <p class="center">3 x täglich 3 - 5 Tabletten unzerkaut mit Wasser zu den Mahlzeiten einnehmen.</p>
  </section>
  <section class="notes notes--hints">
    <h3>Hinweise</h3>
    <ul>
      <li>Die angegebene tägliche Verzehrmenge sollte nicht überschritten werden.</li>
      <li>Nahrungsergänzungsmittel sind kein Ersatz für eine ausgewogene und abwechslungsreiche Ernährung.</li>
      <li>Das Produkt lichtgeschützt, verschlossen und außerhalb der Reichweite von kleinen Kindern aufbewahren.</li>
      <li>Während der Schwangerschaft und Stillzeiten sollte vor dem Verzehr von Nahrungsergän­zungsmitteln ein Arzt konsultiert werden.</li>
    </ul>
  </section>
  <section class="notes notes--expiry">
    <h3>Mindesthaltbarkeitsdatum</h3>
    <p>Siehe Boden.</p>
  </section>
</article>

<!-- blue -->
<article class="label label--blue pos-br">
  <svg class="label__shape" viewBox="0 0 491 228" width="491" height="228" aria-hidden="true">
    <rect class="shape-main" width="491" height="228"/>
    <rect class="shape-accent" width="491" height="14"/>
    <path class="shape-accent" d="M120,206 C250,206 330,180 335,110 C345,185 290,212 210,212 L120,212 Z"/>
    <path class="shape-paper" d="M0,14 H250 C305,18 334,70 330,118 C326,170 285,200 210,204 H0 Z"/>
  </svg>
  <div class="swirl" role="img" aria-label="Abstrakte Spirale in Grüntönen"></div>
  <section class="facts">
    <table>
      <tr><th colspan="3" class="center">Zutaten</th></tr>
      <tr class="gap"><td colspan="3">QUB-Tangen (QUB - Aphanizomenon Flos Aqua) aus dem Klamath Lake, bei 37° Celsius getrocknet.</td></tr>
      <tr><th>Nährwertangaben</th><th class="center">in 100g</th><th class="right">pro Kapsel</th></tr>
      <tr class="nutri"><td colspan="3">Kohlenhydrate<br>Fett<br>Eiweiß<br>Brennwert (kJ / kcal)</td></tr>
      <tr><th>Inhaltsstoffe</th><th class="center">pro Kapsel</th><th class="right">% RDA</th></tr>
      <tr class="vitamin"><td>Vitamin C</td><td class="center">50,2 mg</td><td class="right">50%</td></tr>
    </table>
  </section>
  <address class="distributor"><strong>Vertrieb</strong>Lindor Marsh Trading<br>Weidenhof-Gasse 12<br>1230 Wien<br>Österreich</address>
  <div class="web">www.nuvera-store.example</div>
  <div class="brand"><span class="brand__dot"></span>Nuvera-Store</div>
  <h2 class="product">QUB-Tangen</h2>
  <div class="quantity">100 Tabletten</div>
  <div class="badges"><span class="badge-eu"></span><span class="badge-bio"></span></div>
  <section class="notes notes--usage">
    <h3>Verzehrempfehlung</h3>
    <p class="center">3 x täglich 3 - 5 Tabletten unzerkaut mit Wasser zu den Mahlzeiten einnehmen.</p>
  </section>
  <section class="notes notes--hints">
    <h3>Hinweise</h3>
    <ul>
      <li>Die angegebene tägliche Verzehrmenge sollte nicht überschritten werden.</li>
      <li>Nahrungsergänzungsmittel sind kein Ersatz für eine ausgewogene und abwechslungsreiche Ernährung.</li>
      <li>Das Produkt lichtgeschützt, verschlossen und außerhalb der Reichweite von kleinen Kindern aufbewahren.</li>
      <li>Während der Schwangerschaft und Stillzeiten sollte vor dem Verzehr von Nahrungsergän­zungsmitteln ein Arzt konsultiert werden.</li>
    </ul>
  </section>
  <section class="notes notes--expiry">
    <h3>Mindesthaltbarkeitsdatum</h3>
    <p>Siehe Boden.</p>
  </section>
</article>

</body>
</html>
```